Freelance Translator in Need of a Business Card

I am a freelance Japanese to English translator. I work in the video game localization industry and do literary translation in my spare time. I would like to have both the English word 'Translator' and the Japanese '翻訳者' in the job title. The final design should evoke trust, openness, and reliability.

Target Market(s)

Video game localization companies
Japanese comic book artists

Industry/Entity Type

Business

Contact Information for Business Card

Daniel Ostrowik, Translator
dan.ostrowik@quellbox.net
verolingworks.com
twitter: @verol_tx

Colors

Designer to choose colors to be used in the design.

```html
<!DOCTYPE html>
<html lang="en">
<head>
<meta charset="utf-8">
<title>Daniel Ostrowik — Translator Business Card</title>
<link rel="stylesheet" href="https://fonts.googleapis.com/css2?family=Tinos:ital,wght@0,400;1,700&family=Lato:wght@400&family=Noto+Sans+JP:wght@400&display=swap">
<style>
  :root {
    --stage-bg: #2b2b2b;
    --card-bg: #1d1d1d;
    --card-ink: #ffffff;
    --card-ink-soft: #e6e6e6;
    --frame-line: #f2f2f2;
  }
  * { box-sizing: border-box; margin: 0; padding: 0; }
  html, body {
    width: 1200px;
    height: 1200px;
    overflow: hidden;
    background: var(--stage-bg);
  }
  .stage {
    width: 1200px;
    height: 1200px;
    display: flex;
    flex-direction: column;
    align-items: center;
    justify-content: center;
    gap: 64px;
  }
  .card {
    position: relative;
    width: 820px;
    height: 469px;
    background: var(--card-bg);
    color: var(--card-ink);
    box-shadow: 0 14px 34px rgba(0,0,0,0.45);
  }
  .card__frame {
    position: absolute;
    inset: 30px;
    border: 2px solid var(--frame-line);
    display: flex;
    flex-direction: column;
    align-items: center;
    justify-content: center;
    text-align: center;
  }
  .card__name {
    font-family: "Tinos", "Times New Roman", serif;
    font-weight: 400;
    text-transform: uppercase;
    letter-spacing: 0.04em;
    font-size: 46px;
    line-height: 1;
  }
  .card--back .card__name { font-size: 42px; }
  .card__title {
    margin-top: 10px;
    font-family: "Lato", "Noto Sans JP", sans-serif;
    font-size: 22px;
    color: var(--card-ink-soft);
    letter-spacing: 0.02em;
  }
  .card__title-jp {
    font-family: "Noto Sans JP", sans-serif;
    margin-left: 22px;
  }
  .contact-list {
    list-style: none;
    margin-top: 20px;
    font-family: "Lato", sans-serif;
    font-size: 23px;
    line-height: 1.25;
  }
  .contact-list__label {
    font-family: "Tinos", "Times New Roman", serif;
    font-style: italic;
    font-weight: 700;
    margin-right: 6px;
  }
</style>
</head>
<body>
  <main class="stage">
    <section class="card card--front" aria-label="Business card front">
      <div class="card__frame">
        <h1 class="card__name">Daniel Ostrowik</h1>
      </div>
    </section>

    <section class="card card--back" aria-label="Business card back">
      <div class="card__frame">
        <h2 class="card__name">Daniel Ostrowik</h2>
        <p class="card__title">Translator<span class="card__title-jp" lang="ja">翻訳者</span></p>
        <ul class="contact-list">
          <li><span class="contact-list__label">email:</span>dan.ostrowik@quellbox.net</li>
          <li><span class="contact-list__label">web:</span>verolingworks.com</li>
          <li><span class="contact-list__label">twitter:</span>@verol_tx</li>
        </ul>
      </div>
    </section>
  </main>
</body>
</html>
```